依頼詳細
1.渡航先の選択ページのデザイン
2.出発日の選択ページのデザイン
3.滞在期間の選択ページのデザイン
4.渡航目的の選択ページのデザイン
5.予約方法の選択ページのデザイン

流れが明確であれば、全て繋がった1ページ構成でも結構です

詳しくは添付資料を参照願います
ページ数
5ページ
希望イメージ
シンプル 複雑
単色 カラフル
暗い 明るい
日常 高級
遊び心 厳粛
未来的 伝統的
女性的 男性的
希望する色
青系、濃紺を主にした色合いでお願いいたします
納品ファイル
• 高解像度JPG (.jpg)
補足説明
スクリーンショットおよび、
サイトを構成するファイル一式をご納品いただきます
提案者制限を付加させいただきました
ファイル一式についての補足ですが、AIやPSD等の
画像を作成したツールでの保存形式ファイルもご納品のほどよろしくお願いいたします。
■ 選んだ理由

レベルの高いご提案を頂き、選定に悩みましたが、
「目指すコンセプトとの一致」と作り込み、質問を頂だいた事を鑑みて、選定とさせて頂きました。

■ 提案者全員のお礼・コメント

大変多くのご提案を頂き、どのデザインも甲乙付けがたいご提案で選定に悩みました。
今後また別の機会に、お力添えを頂ければ幸いです。
この度は誠にご提案ありがとうございました。

```html
<!DOCTYPE html>
<html lang="ja">
<head>
<meta charset="UTF-8">
<title>渡航先、出発日、滞在期間の入力</title>
<link rel="stylesheet" href="https://fonts.googleapis.com/css2?family=Noto+Sans+JP:wght@400;500;700&display=swap">
<style>
:root{
  --blue:#3f6fe0;
  --blue-light:#5a8cf0;
  --navy:#0a4aa0;
  --map-blue:#2a67c8;
  --band:#e6e7ea;
  --text:#333;
  --placeholder:#aab0ba;
  --border:#555a63;
  --grey-btn:#c4c6ca;
  --white:#fff;
}
*{box-sizing:border-box;margin:0;padding:0}
html,body{width:1200px;height:3472px;overflow:hidden;background:var(--white)}
body{position:relative;font-family:"Noto Sans JP",sans-serif;color:var(--text)}
.abs{position:absolute}
.top-bar{left:0;top:0;width:1200px;height:132px;background:linear-gradient(90deg,var(--blue-light),var(--blue))}
.menu-icon{left:52px;top:36px}
.title-band{left:0;top:132px;width:1200px;height:116px;background:var(--band);display:flex;align-items:center;justify-content:center;font-size:44px;color:#444}
.step-label{left:48px;font-size:46px}
.check-row{left:48px;display:flex;align-items:center;gap:28px;font-size:46px}
.checkbox{width:58px;height:58px;border:5px solid var(--border);border-radius:8px;display:flex;align-items:center;justify-content:center;background:var(--white)}
.map-area{left:0;top:640px;width:1200px;height:580px;background:radial-gradient(ellipse at 55% 45%,#3b78d6,var(--map-blue) 70%,#fff 100%)}
.slider{left:320px;top:1256px;width:568px;height:30px;border:5px solid #d0d3d8;border-radius:15px;background:#fff}
.slider-fill{left:0;top:0;width:210px;height:100%;background:var(--blue);border-radius:15px}
.field{left:48px;width:1104px;height:112px;border:5px solid var(--border);border-radius:14px;display:flex;align-items:center;padding:0 40px;font-size:42px;color:var(--placeholder);justify-content:space-between;background:#fff}
.select{height:108px;border:5px solid var(--border);border-radius:10px;display:flex;align-items:center;justify-content:space-between;padding:0 40px;font-size:44px;color:var(--text);top:1884px}
.choice{top:2528px;height:112px;border-radius:14px;display:flex;align-items:center;gap:28px;padding-left:40px;font-size:44px}
.choice.selected{left:48px;width:512px;background:var(--blue);color:#fff}
.choice.selected .checkbox{border-color:#fff}
.choice.unselected{left:640px;width:512px;border:5px solid var(--border)}
.btn{display:flex;align-items:center;justify-content:center;border-radius:10px;font-size:48px;color:#fff;font-weight:500}
.btn-next{left:48px;top:2808px;width:1104px;height:140px;background:var(--navy)}
.btn-reset{left:328px;top:3036px;width:548px;height:108px;background:var(--grey-btn)}
.bottom-bar{left:0;top:3360px;width:1200px;height:112px;background:linear-gradient(90deg,var(--blue-light),var(--blue))}
</style>
</head>
<body>
<header class="abs top-bar"></header>
<svg class="abs menu-icon" width="92" height="64" viewBox="0 0 92 64"><g fill="#fff"><rect x="0" y="0" width="92" height="12" rx="3"/><rect x="0" y="26" width="70" height="12" rx="3"/><rect x="0" y="52" width="50" height="12" rx="3"/></g></svg>
<div class="abs title-band">渡航先、出発日、滞在期間の入力</div>

<p class="abs step-label" style="top:370px">1.渡航先を選択してください。（複数選択可能）</p>
<div class="abs check-row" style="top:500px">
  <span class="checkbox"><svg width="40" height="34" viewBox="0 0 40 34"><path d="M4 17l11 11L36 5" fill="none" stroke="#3f6fe0" stroke-width="7"/></svg></span>地図から探す
</div>
<div class="abs map-area" role="img" aria-label="渡航先を選ぶ世界地図（北アメリカを選択中）"></div>
<div class="abs slider"><div class="abs slider-fill"></div></div>

<div class="abs check-row" style="top:1378px"><span class="checkbox"></span>キーワードから探す</div>
<div class="abs field" style="top:1528px">国、地域、都市を入力
  <svg width="48" height="48" viewBox="0 0 48 48"><circle cx="20" cy="20" r="14" fill="none" stroke="#2a5fc0" stroke-width="6"/><path d="M30 30l14 14" stroke="#2a5fc0" stroke-width="7" stroke-linecap="round"/></svg>
</div>

<div class="abs check-row" style="top:1734px"><span class="checkbox"></span>リストから探す</div>
<div class="abs select" style="left:48px;width:516px">地域を選択<svg width="44" height="34" viewBox="0 0 44 34"><path d="M0 0h44L22 34z" fill="#2a5fc0"/></svg></div>
<div class="abs select" style="left:572px;width:580px">国を選択<svg width="44" height="34" viewBox="0 0 44 34"><path d="M0 0h44L22 34z" fill="#2a5fc0"/></svg></div>

<p class="abs step-label" style="top:2062px">2.出発日を選択してください。</p>
<div class="abs field" style="top:2204px;justify-content:flex-end">
  <svg width="64" height="64" viewBox="0 0 64 64"><rect x="4" y="10" width="56" height="50" rx="5" fill="none" stroke="#2a5fc0" stroke-width="5"/><rect x="4" y="10" width="56" height="12" fill="#2a5fc0"/><path d="M18 2v14M46 2v14" stroke="#2a5fc0" stroke-width="5"/><g fill="#2a5fc0"><rect x="13" y="30" width="8" height="7"/><rect x="28" y="30" width="8" height="7"/><rect x="43" y="30" width="8" height="7"/><rect x="13" y="44" width="8" height="7"/><rect x="28" y="44" width="8" height="7"/><rect x="43" y="44" width="8" height="7"/></g></svg>
</div>

<p class="abs step-label" style="top:2394px">3.滞在期間を選択してください。</p>
<div class="abs choice selected"><span class="checkbox"><svg width="34" height="28" viewBox="0 0 40 34"><path d="M4 17l11 11L36 5" fill="none" stroke="#fff" stroke-width="7"/></svg></span>1ヶ月未満</div>
<div class="abs choice unselected"><span class="checkbox"></span>1ヶ月以上</div>

<div class="abs btn btn-next">次へ進む</div>
<div class="abs btn btn-reset">リセット</div>

<footer class="abs bottom-bar"></footer>
</body>
</html>
```